Talvo shoes is a wholesale shoe sales company , mostly working in female shoes and kiddies shoes with a small mens section . looking for a clean slick look. http://www.kemrafootwear.co.za/shop/ is a good reference

It Company

```html
<!DOCTYPE html>
<html lang="en">
<head>
<meta charset="utf-8">
<title>Talvo shoes</title>
<link href="https://fonts.googleapis.com/css2?family=Open+Sans:ital,wght@0,400;0,600;0,700;0,800;1,700;1,800&family=Oswald:wght@500;700&display=swap" rel="stylesheet">
<style>
:root{
  --black:#0d0d0d;
  --red:#e5173f;
  --ink:#222;
  --grey:#777;
  --paper:#fff;
  --page:#ececec;
  --line:#d6d6d6;
  --pink:#f4a3b7;
  --blue:#8fb3e0;
  --fb:#2f5597;
  --tw:#2fa6de;
  --ig:#6f6f6f;
}
*{box-sizing:border-box;margin:0;padding:0}
html,body{width:688px;height:1200px;overflow:hidden}
body{font-family:"Open Sans",Arial,sans-serif;background:var(--page);color:var(--ink);position:relative}
.site{position:absolute;inset:0;width:688px;height:1200px}
/* header */
.topbar{position:absolute;top:0;left:0;width:688px;height:40px;background:var(--black);display:flex;align-items:center;padding:0 16px}
.brand{display:flex;align-items:center;gap:6px;color:#fff;font-weight:800;font-size:20px;letter-spacing:.5px}
.brand-mark{width:12px;height:12px;border-radius:50%;background:#fff}
.top-note{margin-left:auto;color:#ccc;font-size:8px;letter-spacing:.3px;text-transform:uppercase}
.top-note b{color:#fff}
.account{margin-left:10px;display:flex;gap:2px}
.account span{background:#fff;color:#111;font-size:8px;font-weight:700;padding:2px 5px}
.mainnav{position:absolute;top:40px;left:0;width:688px;height:20px;background:var(--black);border-top:1px solid #333;display:flex;align-items:center;padding:0 16px;font-size:9px;color:#fff;font-weight:600}
.mainnav ul{list-style:none;display:flex;gap:12px}
.mainnav .util{margin-left:auto;display:flex;gap:14px;align-items:center}
.cart{display:flex;align-items:center;gap:4px}
/* hero */
.hero{position:absolute;top:60px;left:0;width:688px;height:272px;background:linear-gradient(100deg,#6d625a 0%,#bdb5ad 35%,#e9e6e2 55%,#9a948e 80%,#3f3a36 100%)}
.hero-copy{position:absolute;left:110px;top:92px;text-align:center}
.hero-line{display:inline-block;background:rgba(255,255,255,.85);font-size:15px;color:#444;padding:3px 10px;margin-bottom:3px}
.hero-line.right{margin-left:36px}
.btn-red{display:inline-block;background:var(--red);color:#fff;font-size:9px;font-weight:700;padding:6px 14px;text-transform:uppercase}
.hero-copy .btn-red{margin-top:10px}
.arrow{position:absolute;top:118px;width:16px;height:34px;background:var(--red);display:flex;align-items:center;justify-content:center}
.arrow.prev{left:0}.arrow.next{right:0}
/* promos */
.content{position:absolute;left:28px;top:332px;width:632px;height:760px;background:var(--paper)}
.promos{position:absolute;top:12px;left:4px;display:flex;gap:6px}
.promo{position:relative;width:204px;height:162px;overflow:hidden}
.promo-img{position:absolute;inset:0}
.promo-strap .promo-img{background:linear-gradient(90deg,var(--pink) 0 42%,#e8e4de 42%,#c9b7a9 100%)}
.promo-men .promo-img{background:linear-gradient(90deg,var(--blue) 0 40%,#f3f3f3 40%,#cbb7a4 100%)}
.promo-kids .promo-img{background:linear-gradient(135deg,#6e9bd1,#e6c96b 55%,#c9583f)}
.promo-text{position:absolute;left:8px;top:8px;width:80px}
.promo-text h3{font-size:12px;font-weight:800;color:#fff;line-height:1.1;text-transform:uppercase}
.promo-men .promo-text h3{text-transform:none;color:#fff}
.promo-text p{font-size:6.5px;color:#fff;line-height:1.3;margin:3px 0 6px}
.btn-white{display:inline-block;background:#fff;color:#222;font-size:6.5px;font-weight:700;padding:3px 7px;text-transform:uppercase}
.play-box{position:absolute;right:4px;top:12px;width:92px;background:var(--red);padding:6px 7px;color:#fff}
.play-box h3{font-family:"Oswald",sans-serif;font-size:21px;line-height:1.05;font-weight:700}
.play-box p{font-size:7px;line-height:1.3;margin-top:4px}
/* what's hot */
.hot-head{position:absolute;top:186px;left:0;width:632px;text-align:center}
.hot-head h2{display:inline-block;background:#fff;padding:0 12px;font-style:italic;font-weight:800;font-size:22px;position:relative;z-index:1}
.hot-head::before{content:"";position:absolute;left:30px;right:30px;top:15px;border-top:1px solid var(--line)}
.filters{position:absolute;top:224px;left:4px;width:624px;display:flex;justify-content:space-between}
.select{width:190px;height:18px;border:1px solid #bbb;font-size:7.5px;font-weight:600;display:flex;align-items:center;justify-content:space-between;padding:0 6px}
.select i{border:3px solid transparent;border-top:4px solid #333;margin-top:4px}
.showcase{position:absolute;top:258px;left:82px;width:470px;height:155px;background:linear-gradient(90deg,#7d8a4e,#b8b494 30%,#ddd9cf 50%,#c7c4bf 70%,#5a5550)}
.tag{position:absolute;background:#111;color:#fff;font-size:7px;font-weight:700;padding:3px 6px;text-transform:uppercase}
.showcase .shop{background:#fff;color:#111;font-size:9px;padding:5px 14px;left:197px;top:70px}
/* feed */
.feed-head{position:absolute;top:424px;left:0;width:632px;text-align:center}
.feed-head h2{font-size:17px;font-weight:400;color:#333}
.feed-head h2 b{font-weight:800}
.feed-head h2 span{color:var(--red)}
.feed-head p{font-size:6.5px;color:var(--grey);margin-top:2px}
.products{position:absolute;top:472px;left:34px;display:flex;gap:10px}
.product{width:104px;text-align:center;position:relative}
.product-img{height:100px}
.p1{background:radial-gradient(circle at 50% 60%,#e8cfa3,#fff 70%)}
.p2{background:radial-gradient(circle at 50% 60%,#1c1c1c,#fff 60%)}
.p3{background:radial-gradient(circle at 50% 60%,#c2183b,#fff 60%)}
.p4{background:radial-gradient(circle at 50% 60%,#8a5c3b,#fff 60%)}
.p5{background:radial-gradient(circle at 50% 60%,#8e1f2f,#fff 60%)}
.new{position:absolute;top:0;left:2px;background:var(--red);color:#fff;font-size:6px;font-weight:700;padding:2px 4px}
.price{font-size:11px;font-weight:700;margin-top:6px}
.price s{color:#aaa;font-weight:400;margin-right:4px}
.avail{font-size:6px;color:var(--grey)}
/* newsletter */
.newsletter{position:absolute;top:666px;left:-12px;width:600px;height:72px;background:#f2f2f2;border:1px solid #e1e1e1}
.nl-flag{position:absolute;left:0;top:0;width:24px;height:24px;background:var(--tw)}
.nl-copy{position:absolute;left:32px;top:12px;width:160px}
.nl-copy h3{font-size:16px;font-style:italic;font-weight:700;color:#555}
.nl-copy p{font-size:6.5px;color:var(--grey);line-height:1.3}
.nl-form{position:absolute;left:200px;top:30px;display:flex}
.nl-form .field{width:140px;height:16px;background:#fff;border:1px solid #ccc;font-size:7px;color:#999;padding:3px 5px}
.nl-form .btn-red{font-size:7px;padding:4px 10px}
.nl-img{position:absolute;right:0;top:0;width:140px;height:70px;background:linear-gradient(90deg,#d9c2a0,#333 50%,#b38455)}
/* social + footer */
.social{position:absolute;top:1100px;left:0;width:688px;height:46px;display:flex}
.social a{flex:1;color:#fff;text-decoration:none;font-size:10px;font-weight:600;display:flex;align-items:center;justify-content:center;gap:8px}
.social .sq{width:12px;height:12px;background:#fff;opacity:.9}
.fb{background:var(--fb)}.tw{background:var(--tw)}.ig{background:var(--ig)}
.footer{position:absolute;top:1146px;left:0;width:688px;height:54px;background:#fff;padding:10px 20px;font-size:7px;color:var(--grey)}
.footer ul{list-style:none;display:flex;gap:12px}
.footer p{margin-top:4px}
.cards{position:absolute;right:20px;top:14px;display:flex;gap:4px}
.cards span{width:22px;height:14px;border-radius:2px;background:#9aa5b5}
.cards span:nth-child(2){background:#c8a35c}.cards span:nth-child(3){background:#b07070}.cards span:nth-child(4){background:#7e97b0}
</style>
</head>
<body>
<div class="site">
  <header>
    <div class="topbar">
      <div class="brand"><span class="brand-mark"></span>Talvo shoes</div>
      <div class="top-note">Delivery and returns <b>are always free</b></div>
      <div class="account"><span>Login</span><span>Register</span></div>
    </div>
    <nav class="mainnav">
      <ul><li>Ladies</li><li>Mens</li><li>Girls</li><li>Boys</li><li>Accessories</li><li>Events</li><li>About Talvo</li><li>Stores</li><li>Faq's</li><li>Contact Us</li></ul>
      <div class="util"><span>Order Status</span>
        <span class="cart"><svg width="10" height="9" viewBox="0 0 10 9"><path d="M0 1h2l1.5 5h5L10 2H3" fill="none" stroke="#fff"/><circle cx="4" cy="8" r="1" fill="#fff"/><circle cx="8" cy="8" r="1" fill="#fff"/></svg>My Cart</span></div>
    </nav>
  </header>

  <section class="hero" role="img" aria-label="Hero photo: striped high heel sandal on a desk">
    <div class="arrow prev"><svg width="8" height="10"><path d="M7 0L1 5l6 5z" fill="#fff"/></svg></div>
    <div class="hero-copy">
      <div class="hero-line">You Don't Just Wear It</div><br>
      <div class="hero-line right">You Live It</div><br>
      <span class="btn-red">Shop Now</span>
    </div>
    <div class="arrow next"><svg width="8" height="10"><path d="M1 0l6 5-6 5z" fill="#fff"/></svg></div>
  </section>

  <main class="content">
    <div class="promos">
      <div class="promo promo-strap">
        <div class="promo-img" role="img" aria-label="Pink strappy sandals on a wooden floor"></div>
        <div class="promo-text"><h3>Strap In!</h3><p>Stylish and fun summer sandals for every day</p><span class="btn-white">Shop Now</span></div>
      </div>
      <div class="promo promo-men">
        <div class="promo-img" role="img" aria-label="Brown men's leather shoe"></div>
        <div class="promo-text"><h3>Men's Shoes</h3><p>From casual to dress, we have the style and comfort you need</p><span class="btn-white">Shop Now</span></div>
      </div>
      <div class="promo promo-kids">
        <div class="promo-img" role="img" aria-label="Child playing outdoors in sneakers"></div>
        <div class="play-box"><h3>Time to Play!</h3><p>Our durable sneakers go from classroom to playground</p></div>
      </div>
    </div>

    <div class="hot-head"><h2>What's hot!</h2></div>
    <div class="filters">
      <div class="select">Women's New Collection<i></i></div>
      <div class="select">Men's New Collection<i></i></div>
      <div class="select">Kids's New Collection<i></i></div>
    </div>

    <div class="showcase" role="img" aria-label="Fashion photo: woman outdoors and man seated in a suit">
      <span class="tag" style="left:70px;top:72px">Women</span>
      <span class="tag shop">Shop Now</span>
      <span class="tag" style="left:344px;top:72px">Men</span>
    </div>

    <div class="feed-head">
      <h2><span>Be Inspired</span> <b>Talvo's</b> Live Purchase Feed</h2>
      <p>Check out the latest purchases from shoppers across the country, updated live as orders come in every day</p>
    </div>

    <div class="products">
      <div class="product"><span class="new">NEW</span><div class="product-img p1" role="img" aria-label="Gold embellished high heel"></div><div class="price"><s>$120.00</s>$99.00</div><div class="avail">available in more colors</div></div>
      <div class="product"><div class="product-img p2" role="img" aria-label="Black patent stiletto pump"></div><div class="price">$120.00</div><div class="avail">available in more colors</div></div>
      <div class="product"><span class="new">NEW</span><div class="product-img p3" role="img" aria-label="Red platform high heel"></div><div class="price"><s>$120.00</s>$99.00</div><div class="avail">available in more colors</div></div>
      <div class="product"><div class="product-img p4" role="img" aria-label="Brown fur-trim ankle boot"></div><div class="price">$120.00</div><div class="avail">available in more colors</div></div>
      <div class="product"><div class="product-img p5" role="img" aria-label="Burgundy knee high boot"></div><div class="price">$120.00</div><div class="avail">available in more colors</div></div>
    </div>

    <section class="newsletter">
      <div class="nl-flag"></div>
      <div class="nl-copy"><h3>Newsletter</h3><p>Stay informed. Join our email list to get news on new arrivals and our monthly shoe giveaway</p></div>
      <div class="nl-form"><div class="field">Email Address</div><span class="btn-red">Sign Up</span></div>
      <div class="nl-img" role="img" aria-label="Assorted women's shoes"></div>
    </section>
  </main>

  <div class="social">
    <a class="fb"><span class="sq"></span>Follow Us on Facepage</a>
    <a class="tw"><span class="sq"></span>Follow Us on Chirper</a>
    <a class="ig"><span class="sq"></span>Follow Us on Snapgram</a>
  </div>

  <footer class="footer">
    <ul><li>Terms &amp; Conditions</li><li>About Us</li><li>Delivery and Returns</li><li>Contact Us</li></ul>
    <p>© 2012 Talvo Shoes. All Rights Reserved.</p>
    <div class="cards"><span></span><span></span><span></span><span></span><span></span></div>
  </footer>
</div>
</body>
</html>
```